Kestin Power Battery advertisment for Facebook ads

Objective:
Design a compelling Facebook advertisement to promote the new Federal Government Home Battery Subsidy, encouraging existing solar customers to act now and install a battery system under the new subsidy program.

Key Message:

25kWh Battery System Installed from $9,800
Act now and secure your affordable energy future today!
Design Requirements:

Bold headline showcasing the 25kWh for $9,800 offer.
Clear reference to the Federal Government Battery Subsidy as the reason for the low pricing.
Include messaging around:
Claim your subsidy before it winds down—like the solar rebate, it reduces each year
The subsidy can only be claimed once per household—go large now to future-proof your energy needs
Add a strong Call to Action like: “Beat the Rush—Secure Your Battery Today!”

Target Market(s)

Home owners who want to add batteries to existing solar systems

Industry/Entity Type

Renewable energy

Colors
0054AA
0677BA
7BADD7
CADEEF
E8F1F8
EB3D1F
EC4F4E
F09395
F8D3D4
FCEDEE

Requirements
Must have
• Visual Style: Modern, clean, and high-trust Use imagery of solar homes, battery units, or families enjoying power security at night Include visual cues of savings, energy independence, or clean energy Mobile-optimized, designed for Facebook feed
Nice to have
• Tone: Confident, future-focused, and urgent—while remaining trustworthy and informative. I would like a picture of battery ideally VOM battery on a home or such
Should not have
• must be professional and be a call to action

```html
<!DOCTYPE html>
<html lang="en">
<head>
<meta charset="UTF-8">
<title>Kestin Power – 25kWh Home Battery Offer</title>
<link href="https://fonts.googleapis.com/css2?family=Archivo:wght@800&family=Inter:wght@400;600;700&display=swap" rel="stylesheet">
<style>
  :root {
    --sky-top: #a9d3f2;
    --sky-mid: #e3f0fa;
    --sky-low: #ffffff;
    --ink: #0a0a0a;
    --offer-red: #e8090f;
    --offer-red-deep: #b8060b;
    --grass-top: #6f9a3c;
    --grass-bottom: #2f5a1a;
    --unit-light: #f4f5f6;
    --unit-shade: #d9dcdf;
    --white: #ffffff;
  }
  * { margin: 0; padding: 0; box-sizing: border-box; }
  html, body { width: 1200px; height: 1200px; overflow: hidden; }
  body { font-family: "Inter", Arial, sans-serif; color: var(--ink); }

  .ad {
    position: relative;
    width: 1200px;
    height: 1200px;
    overflow: hidden;
    background: linear-gradient(180deg, var(--sky-top) 0%, var(--sky-mid) 18%, var(--sky-low) 42%, var(--sky-low) 100%);
  }

  .ground {
    position: absolute;
    left: 0; right: 0; top: 1006px; bottom: 0;
    background: linear-gradient(180deg, var(--grass-top) 0%, var(--grass-bottom) 100%);
  }

  .headline {
    position: absolute;
    left: 74px; top: 158px;
    font-family: "Archivo", Arial, sans-serif;
    font-weight: 800;
    font-size: 114px;
    line-height: 131px;
    letter-spacing: -1px;
    white-space: nowrap;
  }
  .headline .accent { color: var(--offer-red); }

  .subsidy-note {
    position: absolute;
    left: 76px; top: 626px;
    width: 720px;
    font-size: 40px;
    line-height: 50px;
    font-weight: 400;
  }

  .cta {
    position: absolute;
    left: 76px; top: 868px;
    width: 498px; height: 94px;
  }
  .cta-shadow {
    position: absolute;
    left: 13px; top: 17px;
    width: 100%; height: 100%;
    background: var(--offer-red-deep);
    border-radius: 14px;
  }
  .cta-face {
    position: absolute;
    inset: 0;
    background: var(--offer-red);
    border-radius: 14px;
    color: var(--white);
    font-weight: 600;
    font-size: 38px;
    line-height: 36px;
    padding: 11px 0 0 43px;
    white-space: nowrap;
  }

  .brand {
    position: absolute;
    left: 100px; top: 1060px;
    display: flex;
    flex-direction: column;
  }
  .brand-name {
    font-weight: 700;
    font-size: 40px;
    line-height: 44px;
    color: var(--white);
  }
  .brand-tagline {
    font-size: 13px;
    color: var(--white);
    margin-top: 6px;
  }

  .battery-unit {
    position: absolute;
    left: 787px; top: 542px;
    width: 335px; height: 608px;
    border-radius: 10px 10px 4px 4px;
    background: linear-gradient(90deg, var(--unit-light) 0%, var(--white) 45%, var(--unit-shade) 100%);
  }
</style>
</head>
<body>
  <main class="ad">
    <div class="ground" role="img" aria-label="Green grass field along the bottom"></div>

    <h1 class="headline">
      <span class="accent">25kWh</span> Home<br>
      Battery Installed<br>
      from <span class="accent">$9,800</span>
    </h1>

    <p class="subsidy-note">Thanks to the Federal Government<br>Subsidy—Act Now Before It<br>Reduces!</p>

    <div class="cta">
      <div class="cta-shadow"></div>
      <div class="cta-face">Beat the Rush—Secure<br>Your Battery Today!</div>
    </div>

    <div class="brand">
      <span class="brand-name">Kestin Power</span>
      <span class="brand-tagline">Home energy storage specialists</span>
    </div>

    <div class="battery-unit" role="img" aria-label="White stacked home battery unit standing on the grass"></div>
  </main>
</body>
</html>
```